Odvetnik - Attorney at law
Sodni tolmač za angleški jezik - English language Court Interpreter
Simple
Marjan Lesk
Odvetnik - Attorney at law Sodni tolmač za angleški jezik - English Language Court Interpreter
Brinjeva ulica 41 6000 Koper Slovenija
info@marjanlesk.example
www.marjanlesk.example
I invite all designers under logo project Attorney Marjan Lesk to participate. Please inform all designers.

```html
<!DOCTYPE html>
<html lang="sl">
<head>
<meta charset="utf-8">
<title>Marjan Lesk – Business Card</title>
<link rel="stylesheet" href="https://fonts.googleapis.com/css2?family=Arimo:wght@400&family=Marcellus&display=swap">
<style>
  :root {
    --backdrop: #2b2b2d;
    --card: #ffffff;
    --navy: #3c3a7c;
    --orange: #f7941d;
    --ink: #34336f;
    --on-band: #ffffff;
  }
  * { margin: 0; padding: 0; box-sizing: border-box; }
  html, body {
    width: 1200px;
    height: 1052px;
    overflow: hidden;
    background: var(--backdrop);
  }
  .business-card {
    position: absolute;
    left: 100px;
    top: 226px;
    width: 1000px;
    height: 600px;
    background: var(--card);
    border-radius: 30px;
    overflow: hidden;
    font-family: "Arimo", Arial, sans-serif;
  }
  .brand {
    position: absolute;
    left: 170px;
    top: 78px;
    display: flex;
    align-items: center;
    gap: 26px;
  }
  .brand-square {
    width: 62px;
    height: 62px;
    background: var(--orange);
  }
  .brand-name {
    font-family: "Marcellus", Georgia, serif;
    font-size: 70px;
    letter-spacing: 2px;
    color: var(--navy);
    line-height: 1;
  }
  .contact-band {
    position: absolute;
    left: 0;
    top: 252px;
    width: 100%;
    height: 160px;
    display: flex;
    color: var(--on-band);
  }
  .address-block {
    width: 400px;
    flex: none;
    background: var(--orange);
    padding: 26px 22px 0 0;
    text-align: right;
    font-size: 26px;
    line-height: 33px;
    white-space: nowrap;
  }
  .details-block {
    flex: 1;
    background: var(--navy);
    padding: 20px 0 0 44px;
    font-size: 26px;
    line-height: 30px;
    white-space: nowrap;
  }
  .detail-row { display: flex; }
  .detail-label { width: 84px; }
  .services {
    position: absolute;
    left: 150px;
    top: 462px;
    color: var(--ink);
    font-size: 25px;
    line-height: 34px;
  }
</style>
</head>
<body>
  <article class="business-card">
    <div class="brand">
      <span class="brand-square"></span>
      <span class="brand-name">MARJAN LESK</span>
    </div>

    <div class="contact-band">
      <div class="address-block">
        <p>Brinjeva ulica 41</p>
        <p>6000 Koper, Slovenija</p>
        <p>www.marjanlesk.example</p>
      </div>
      <div class="details-block">
        <p class="detail-row"><span class="detail-label">Ph.</span><span>+386 5 5550142</span></p>
        <p class="detail-row"><span class="detail-label">Cell</span><span>+386 40555187</span></p>
        <p class="detail-row"><span class="detail-label">Fax</span><span>+386 5 5550143</span></p>
        <p class="detail-row"><span class="detail-label">Email</span><span>info@marjanlesk.example</span></p>
      </div>
    </div>

    <div class="services">
      <p>Odvetnik Attorney at law</p>
      <p>Sodni tolmač za angleški jezik English language Court Interpreter</p>
    </div>
  </article>
</body>
</html>
```